Business card design needed & Logo Design for Marketing

We need a business card design for a new beauty business. We offer Eyelash Extensions and beauty services, from our relaxing home based salon.

I would like the design to be modern and contemporary but with a twist of vintage thrown in. Our fave colour is Spearmint.

I also need a logo that can be embroidered onto uniforms.

Contact Information for Business Card

Willow Bloom Beauty
Eyelash Extensions and Beauty Services
18 Tindarra Crescent, Hollybank 4815
0418562971

```html
<!DOCTYPE html>
<html lang="en">
<head>
<meta charset="utf-8">
<title>Willow Bloom Beauty – Business Card</title>
<link rel="stylesheet" href="https://fonts.googleapis.com/css2?family=Arimo:wght@400;700&display=swap">
<style>
  :root {
    --spearmint: #6fc2a1;
    --spearmint-light: #7dccae;
    --spearmint-deep: #66b897;
    --ink: #231f20;
    --paper: #f4f4f2;
  }
  html, body {
    margin: 0;
    padding: 0;
    width: 1200px;
    height: 741px;
    overflow: hidden;
    background: var(--spearmint);
  }
  .card {
    position: relative;
    width: 1200px;
    height: 741px;
    overflow: hidden;
    background:
      radial-gradient(ellipse 900px 260px at 20% 10%, var(--spearmint-light) 0%, transparent 70%),
      radial-gradient(ellipse 700px 300px at 90% 85%, var(--spearmint-light) 0%, transparent 70%),
      linear-gradient(160deg, var(--spearmint) 0%, var(--spearmint-deep) 55%, var(--spearmint) 100%);
    font-family: "Arimo", Arial, sans-serif;
  }
  .brand {
    position: absolute;
    left: 0;
    right: 0;
    top: 215px;
    text-align: center;
    color: var(--ink);
    font-family: "Arimo", Arial, sans-serif;
    font-weight: 700;
    font-size: 84px;
    line-height: 1.1;
    letter-spacing: 1px;
    margin: 0;
  }
  .services {
    position: absolute;
    left: 0;
    right: 0;
    top: 540px;
    margin: 0;
    text-align: center;
    color: var(--paper);
    font-weight: 400;
    font-size: 35px;
    letter-spacing: 0.2px;
  }
  .services .divider {
    display: inline-block;
    width: 3px;
    height: 22px;
    margin: 0 24px;
    background: var(--ink);
    vertical-align: 1px;
  }
</style>
</head>
<body>
  <main class="card">
    <h1 class="brand">Willow Bloom<br>Beauty</h1>
    <p class="services">Eyelash Extensions<span class="divider" aria-hidden="true"></span>Waxing Services</p>
  </main>
</body>
</html>
```